PLM - Business Card Design Project

We need a business card based on our logo
Updates

Hi I just upload logo file in AI format Thanks and regards

Target Market(s)

Bank, Big companies, Business owners

Industry/Entity Type

Business

Font styles to use
Sans Serif

```html
<!DOCTYPE html>
<html lang="fr">
<head>
<meta charset="utf-8">
<title>PLM – Carte de visite</title>
<link rel="stylesheet" href="https://fonts.googleapis.com/css2?family=Questrial&display=swap">
<style>
  :root {
    --card-white: #ffffff;
    --navy: #14134a;
    --logo-navy: #1c2d5c;
    --dot-light: #b9dcf3;
    --dot-mid: #8cc3ea;
    --dot-deep: #5aaee0;
    --text-light: #ffffff;
  }
  html, body {
    margin: 0;
    padding: 0;
    width: 1200px;
    height: 799px;
    overflow: hidden;
    background: var(--card-white);
    font-family: "Questrial", sans-serif;
  }
  .card {
    position: relative;
    width: 1200px;
    height: 799px;
    background: var(--card-white);
    overflow: hidden;
  }
  .card__pattern,
  .card__band {
    position: absolute;
    inset: 0;
    width: 1200px;
    height: 799px;
  }
  .brand {
    position: absolute;
    left: 455px;
    top: 175px;
    color: var(--logo-navy);
  }
  .brand__name {
    display: block;
    font-size: 150px;
    line-height: 1;
    letter-spacing: -2px;
  }
  .brand__firm {
    display: block;
    font-size: 30px;
    margin-top: 6px;
  }
  .brand__tagline {
    display: block;
    font-size: 18px;
    margin-top: 2px;
    padding-left: 20px;
  }
  .contact {
    position: absolute;
    left: 60px;
    top: 560px;
    display: flex;
    align-items: flex-start;
    color: var(--text-light);
  }
  .contact__firm {
    font-size: 30px;
    margin-top: 6px;
    white-space: nowrap;
  }
  .contact__divider {
    width: 2px;
    height: 96px;
    background: var(--text-light);
    margin: 0 24px 0 30px;
  }
  .contact__address {
    font-size: 26px;
    line-height: 1.2;
    font-style: normal;
    padding-top: 8px;
    white-space: nowrap;
  }
</style>
</head>
<body>
  <main class="card">
    <svg class="card__pattern" viewBox="0 0 1200 799" role="img" aria-label="Motif décoratif de points bleus dégradés">
      <defs>
        <radialGradient id="pattern-left" cx="0.3" cy="0.3" r="0.7">
          <stop offset="0" stop-color="var(--dot-mid)" stop-opacity="0.85"/>
          <stop offset="0.6" stop-color="var(--dot-light)" stop-opacity="0.55"/>
          <stop offset="1" stop-color="var(--dot-light)" stop-opacity="0"/>
        </radialGradient>
        <radialGradient id="pattern-right" cx="0.7" cy="0.5" r="0.65">
          <stop offset="0" stop-color="var(--dot-deep)" stop-opacity="0.75"/>
          <stop offset="0.6" stop-color="var(--dot-light)" stop-opacity="0.5"/>
          <stop offset="1" stop-color="var(--dot-light)" stop-opacity="0"/>
        </radialGradient>
      </defs>
      <ellipse cx="200" cy="130" rx="330" ry="230" fill="url(#pattern-left)"/>
      <ellipse cx="980" cy="320" rx="330" ry="240" fill="url(#pattern-right)"/>
    </svg>

    <svg class="card__band" viewBox="0 0 1200 799" aria-hidden="true">
      <path d="M0,430 Q600,400 1200,700 L1200,799 L0,799 Z" fill="var(--navy)"/>
    </svg>

    <header class="brand">
      <span class="brand__name">PLM</span>
      <span class="brand__firm">Cabinet Perrin &amp; Martel</span>
      <span class="brand__tagline">Expertise-Comptable.Audit.Conseil</span>
    </header>

    <section class="contact">
      <span class="contact__firm">Cabinet Perrin &amp; Martel</span>
      <span class="contact__divider"></span>
      <address class="contact__address">
        1840 W Sandstone Avenue Suite<br>
        4 Boulder City<br>
        Nevada 89005
      </address>
    </section>
  </main>
</body>
</html>
```